Custom Woodworking and Rock Design

We specialize in original, high quality, wood and rock art. It’s should be self explanatory ask questions if you need. Your team designing a logo. Furniture is custom made to order. Rocks are designed depending on consumer needs. Wood and rock can also be combined for custom work. Painted rocks on vintage wood. Custom chairs and cabinets. Artistic rocks for multiple uses:garden, magnets, custom. All ideas and requests are welcome.

Target Market(s)

All

Contact Information for Business Card

Mara Dolby
Talverstonecraft@mailvoro.net

Font styles to use
Sans Serif

Requirements
Must have
• Clear lettering
Nice to have
• Eye catching
Should not have
• Blurr

```html
<!DOCTYPE html>
<html lang="en">
<head>
<meta charset="utf-8">
<title>Talver Stonecraft – Business Card</title>
<link href="https://fonts.googleapis.com/css2?family=Oswald:wght@500&family=Questrial&display=swap" rel="stylesheet">
<style>
  :root {
    --backdrop: #1c1c1c;
    --card: #262727;
    --card-edge: #1e1f1f;
    --accent: #1a7fd0;
    --ink: #f2f2f2;
  }
  * { margin: 0; padding: 0; box-sizing: border-box; }
  html, body {
    width: 1200px;
    height: 900px;
    overflow: hidden;
    background: var(--backdrop);
  }
  .stage {
    position: relative;
    width: 1200px;
    height: 900px;
  }
  .card {
    position: absolute;
    left: 270px;
    width: 660px;
    height: 340px;
    background: linear-gradient(135deg, var(--card-edge) 0%, var(--card) 60%, #2f3030 100%);
    border-bottom: 5px solid var(--accent);
    box-shadow: 0 14px 30px rgba(0,0,0,.55);
    font-family: "Questrial", "Century Gothic", sans-serif;
    color: var(--ink);
  }
  .card--front { top: 90px; }
  .card--back  { top: 465px; }

  /* Front */
  .brand {
    position: absolute;
    inset: 0;
    display: flex;
    align-items: center;
    justify-content: center;
    gap: 16px;
  }
  .brand__square {
    width: 22px;
    height: 22px;
    background: var(--accent);
  }
  .brand__name {
    font-size: 44px;
    letter-spacing: 1px;
    color: var(--ink);
  }

  /* Back */
  .person {
    position: absolute;
    right: 370px;
    top: 128px;
    text-align: right;
  }
  .person__name {
    font-family: "Oswald", "Arial Narrow", sans-serif;
    font-weight: 500;
    font-size: 36px;
    line-height: 1;
    letter-spacing: 1px;
    text-transform: uppercase;
    color: var(--accent);
  }
  .person__role {
    margin-top: 8px;
    font-size: 17px;
    letter-spacing: .5px;
  }
  .divider {
    position: absolute;
    left: 318px;
    top: 126px;
    width: 2px;
    height: 86px;
    background: var(--accent);
  }
  .contact {
    position: absolute;
    left: 342px;
    top: 134px;
    list-style: none;
  }
  .contact__item {
    display: flex;
    align-items: center;
    gap: 9px;
    font-size: 16px;
    letter-spacing: .5px;
    line-height: 24px;
  }
  .contact__icon {
    width: 12px;
    height: 12px;
    flex: none;
    fill: none;
    stroke: var(--accent);
    stroke-width: 1.4;
  }
</style>
</head>
<body>
<main class="stage">
  <section class="card card--front" aria-label="Card front">
    <div class="brand">
      <span class="brand__square"></span>
      <span class="brand__name">Talver Stonecraft</span>
    </div>
  </section>

  <section class="card card--back" aria-label="Card back">
    <div class="person">
      <p class="person__name">Mara Dolby</p>
      <p class="person__role">Director</p>
    </div>
    <span class="divider"></span>
    <ul class="contact">
      <li class="contact__item">
        <svg class="contact__icon" viewBox="0 0 12 12"><path d="M3 1 L5 3.5 L4 5 Q5.5 7.5 7 8 L8.5 7 L11 9 L9.5 11 Q4 10.5 1 2.5 Z"/></svg>
        +330 4418-2053
      </li>
      <li class="contact__item">
        <svg class="contact__icon" viewBox="0 0 12 12"><rect x="1" y="2.5" width="10" height="7"/><path d="M1 2.5 L6 7 L11 2.5"/></svg>
        Talverstonecraft@mailvoro.net
      </li>
      <li class="contact__item">
        <svg class="contact__icon" viewBox="0 0 12 12"><circle cx="6" cy="6" r="5"/><ellipse cx="6" cy="6" rx="2.2" ry="5"/><path d="M1 6 H11 M2 3.5 H10 M2 8.5 H10"/></svg>
        www.talverstonecraft.net
      </li>
    </ul>
  </section>
</main>
</body>
</html>
```